Business card

I want a business card the looks like a credit card, must eye-catching !!! I attached some things that I did obviously I want it to LOOK WAY more professional than what I can do....Just some ideas.... that I was thinking

Contact Information for Business Card

Must look like a credit card, I attached some things that I did obviously I want it to LOOK WAY more professional than what I can do....Just some ideas.... that I was thinking

Requirements
Must have
• Must look like a credit card, I attached some things that I did obviously I want it to LOOK WAY more professional than what I can do....Just some ideas.... that I was thinking
Nice to have
Should not have

```html
<!DOCTYPE html>
<html lang="en">
<head>
<meta charset="utf-8">
<title>Relaunch Commerce Group – Business Card</title>
<link rel="stylesheet" href="https://fonts.googleapis.com/css2?family=Lato:wght@400;700;900&display=swap">
<style>
  :root {
    --page-bg: #2b2b2e;
    --navy-deep: #141d5e;
    --navy: #1f3590;
    --blue: #3a5cc0;
    --blue-light: #8fb0ec;
    --gold: #f6c81b;
    --white: #ffffff;
    --chip: #fbfaf6;
    --chip-line: #8a5a2a;
  }
  * { box-sizing: border-box; margin: 0; padding: 0; }
  html, body { width: 1200px; height: 900px; overflow: hidden; }
  body {
    background: var(--page-bg);
    font-family: "Lato", sans-serif;
    display: flex;
    flex-direction: column;
    align-items: center;
    justify-content: center;
    gap: 36px;
  }
  .card {
    position: relative;
    width: 640px;
    height: 404px;
    border-radius: 22px;
    overflow: hidden;
    background: linear-gradient(150deg, var(--blue) 0%, var(--navy) 48%, var(--navy-deep) 100%);
    color: var(--white);
  }
  .card__waves { position: absolute; inset: 0; width: 100%; height: 100%; }
  .brand {
    position: absolute;
    display: flex;
    flex-direction: column;
    align-items: flex-start;
  }
  .brand__services {
    font-weight: 900;
    font-size: 10px;
    letter-spacing: 0.04em;
    text-transform: uppercase;
    color: var(--white);
    white-space: nowrap;
  }
  .brand__name-row { display: flex; align-items: center; gap: 10px; }
  .brand__dot { width: 22px; height: 22px; border-radius: 50%; background: var(--gold); flex: none; }
  .brand__name {
    font-weight: 900;
    color: var(--gold);
    line-height: 1.05;
    white-space: nowrap;
  }
  .card--front .brand { left: 100px; top: 138px; }
  .card--front .brand__name { font-size: 34px; }
  .card--back .brand { right: 40px; top: 38px; align-items: flex-end; }
  .card--back .brand__name { font-size: 26px; }
  .brand__services-row { display: flex; gap: 18px; margin: 5px 0; }
  .chip { position: absolute; left: 70px; top: 150px; width: 124px; height: 92px; }
  .holder { position: absolute; left: 54px; bottom: 50px; }
  .holder__name { font-weight: 900; font-size: 32px; color: var(--gold); letter-spacing: 0.02em; }
  .holder__role { font-size: 18px; color: var(--white); margin-top: 2px; }
  .contact {
    position: absolute;
    right: 40px;
    top: 148px;
    list-style: none;
    text-align: right;
    font-size: 17px;
    line-height: 1.5;
  }
  .contact li { display: flex; justify-content: flex-end; align-items: center; gap: 10px; white-space: nowrap; }
  .contact__icon { width: 16px; height: 16px; flex: none; }
  .contact__spacer { width: 16px; flex: none; }
</style>
</head>
<body>

<section class="card card--front" aria-label="Card front">
  <svg class="card__waves" viewBox="0 0 640 404" preserveAspectRatio="none" aria-hidden="true">
    <path d="M0 250 C160 120 360 60 640 90 L640 0 L0 0 Z" fill="#6f90e0" opacity="0.25"/>
    <path d="M120 404 C140 260 320 170 640 190" stroke="#b9cdf5" stroke-width="2" fill="none" opacity="0.5"/>
    <path d="M60 404 C120 220 300 110 640 120" stroke="#b9cdf5" stroke-width="1.5" fill="none" opacity="0.4"/>
    <path d="M220 404 C230 300 420 230 640 250 L640 404 Z" fill="#0f1850" opacity="0.35"/>
    <path d="M0 90 C200 40 380 30 520 0" stroke="#c9d8f8" stroke-width="1.5" fill="none" opacity="0.35"/>
  </svg>
  <div class="brand">
    <div class="brand__services-row">
      <span class="brand__services">Business Broker</span>
      <span class="brand__services">Business Funding</span>
    </div>
    <div class="brand__name-row">
      <span class="brand__dot"></span>
      <span class="brand__name">Relaunch Commerce Group</span>
    </div>
    <div class="brand__services-row">
      <span class="brand__services">Credit Card Processing</span>
      <span class="brand__services">Merchant Broker</span>
    </div>
  </div>
</section>

<section class="card card--back" aria-label="Card back">
  <svg class="card__waves" viewBox="0 0 640 404" preserveAspectRatio="none" aria-hidden="true">
    <path d="M0 300 C180 160 380 120 640 150 L640 0 L0 0 Z" fill="#6f90e0" opacity="0.22"/>
    <path d="M140 404 C160 280 340 200 640 215" stroke="#b9cdf5" stroke-width="2" fill="none" opacity="0.45"/>
    <path d="M60 404 C110 240 300 140 640 140" stroke="#b9cdf5" stroke-width="1.5" fill="none" opacity="0.4"/>
    <path d="M260 404 C270 320 440 260 640 270 L640 404 Z" fill="#0f1850" opacity="0.35"/>
  </svg>

  <div class="brand">
    <div class="brand__services-row">
      <span class="brand__services">Business Broker</span>
      <span class="brand__services">Business Funding</span>
    </div>
    <div class="brand__name-row">
      <span class="brand__dot"></span>
      <span class="brand__name">Relaunch Commerce Group</span>
    </div>
    <div class="brand__services-row">
      <span class="brand__services">Credit Card Processing</span>
      <span class="brand__services">Merchant Broker</span>
    </div>
  </div>

  <svg class="chip" viewBox="0 0 100 76" aria-hidden="true">
    <rect x="1" y="1" width="98" height="74" rx="12" fill="var(--chip)" stroke="var(--chip-line)" stroke-width="1.5"/>
    <g stroke="var(--chip-line)" stroke-width="1.2" fill="none">
      <path d="M1 25 H35 M1 50 H35 M65 25 H99 M65 50 H99"/>
      <path d="M35 1 V75 M65 1 V75"/>
      <rect x="35" y="20" width="30" height="36" rx="12"/>
    </g>
  </svg>

  <ul class="contact">
    <li>1234 First Line Address<span class="contact__spacer"></span></li>
    <li>5678 Second Line Address<span class="contact__spacer"></span></li>
    <li>1234567890
      <svg class="contact__icon" viewBox="0 0 16 16" aria-hidden="true"><path d="M3 1 L6 1 L7 5 L5 6 C6 8 8 10 10 11 L11 9 L15 10 L15 13 C15 14 14 15 13 15 C6 15 1 10 1 3 C1 2 2 1 3 1 Z" fill="var(--gold)"/></svg>
    </li>
    <li>info@yourmail.com
      <svg class="contact__icon" viewBox="0 0 16 16" aria-hidden="true"><rect x="1" y="3" width="14" height="10" fill="var(--gold)"/><path d="M1 3 L8 9 L15 3" stroke="var(--navy-deep)" stroke-width="1.2" fill="none"/></svg>
    </li>
    <li>www.yourwebsite.com
      <svg class="contact__icon" viewBox="0 0 16 16" aria-hidden="true"><circle cx="8" cy="8" r="7" fill="none" stroke="var(--gold)" stroke-width="1.5"/><path d="M1 8 H15 M8 1 C4 5 4 11 8 15 M8 1 C12 5 12 11 8 15" stroke="var(--gold)" stroke-width="1.1" fill="none"/></svg>
    </li>
  </ul>

  <div class="holder">
    <p class="holder__name">TAVIN ROURKE</p>
    <p class="holder__role">Founder</p>
  </div>
</section>

</body>
</html>
```